hotel's Website

Hotels website redesign for reference pictures, logo etc see http://restwellmarlow.co.uk/

1. 2-3 Special offers on the main page.
2. Booking calender
3. Location Map
4. Picture gallery.
5. Journeyscope reviews.
6. short description
7. Social Media sharing.
8 Phone number and address.

Industry/Entity Type

Hotel

Requirements
Must have
• 1. 2-3 Special offers on the main page.
2. Booking calender
3. Location Map
4. Picture gallery.
5. Journeyscope reviews.
6. short description
7. Social Media sharing.

```html
<!DOCTYPE html>
<html lang="en">
<head>
<meta charset="utf-8">
<title>Restwell Inn London - Victoria</title>
<link href="https://fonts.googleapis.com/css2?family=Montserrat:wght@400;600;700&family=Open+Sans:wght@400;600;700&display=swap" rel="stylesheet">
<style>
:root{
  --panel:rgba(28,28,32,.93);
  --white:#ffffff;
  --ink:#2b2b2b;
  --muted:#8a8a8a;
  --text-light:#d6d6d6;
  --orange:#e8431f;
  --brand-blue:#1257a8;
  --button-blue:#1e8fd6;
  --review-green:#58a444;
  --link-blue:#3a6ab5;
  --field-border:#d4d4d4;
}
*{margin:0;padding:0;box-sizing:border-box}
html,body{width:858px;height:1200px;overflow:hidden}
body{position:relative;font-family:'Open Sans',sans-serif;color:var(--white)}
.backdrop{position:absolute;inset:0;background:linear-gradient(180deg,#b9c3cc 0%,#8f9488 18%,#6f7566 45%,#7b7e78 70%,#8c9199 100%)}
.abs{position:absolute}
.brand-mark{width:78px;height:89px;background:var(--brand-blue);display:flex;align-items:center;justify-content:center}
.brand-mark .name{font-family:'Montserrat',sans-serif;font-weight:600;font-size:13px;color:var(--white);text-align:center;line-height:1.2}
.place-title{font-family:'Montserrat',sans-serif;font-weight:600;font-size:14px;letter-spacing:3px;white-space:nowrap}
.section{position:absolute;left:118px;width:623px;background:var(--panel)}
.main-nav{top:113px;height:50px;display:flex;align-items:center;justify-content:space-between;padding:0 18px 0 18px}
.main-nav a,.footer-nav a{font-family:'Montserrat',sans-serif;font-size:8px;font-weight:600;letter-spacing:1.3px;color:var(--white);text-decoration:none;white-space:nowrap}
.hero{top:163px;height:149px;background:linear-gradient(100deg,#3b2e26 0%,#8a5a3a 30%,#c9a45c 55%,#e8d9a8 75%,#b8762e 100%)}
.slide-arrow{position:absolute;top:232px;width:22px;height:22px}
.caption{position:absolute;left:55px;top:86px;width:390px;height:53px;background:var(--orange);padding:5px 7px;font-family:'Montserrat',sans-serif;white-space:nowrap}
.caption h2{font-size:12px;font-weight:700;letter-spacing:1px}
.caption p{font-size:11px;letter-spacing:.7px;line-height:1.3}
.booking-band{top:312px;height:84px}
.booking{position:absolute;left:17px;top:17px;width:590px;height:49px;background:var(--white);color:var(--ink)}
.booking h3{position:absolute;left:25px;top:9px;font-family:'Montserrat',sans-serif;font-size:10.5px;font-weight:600;letter-spacing:.5px}
.booking .intro{position:absolute;left:25px;top:22px;font-size:7.5px;color:var(--muted);line-height:1.3;width:90px}
.field-label{position:absolute;top:6px;font-size:7.5px;color:var(--muted);white-space:nowrap}
.field{position:absolute;top:21px;height:22px;border:1px solid var(--field-border);font-size:7.5px;color:var(--muted);padding:6px 7px;white-space:nowrap}
.book-btn{position:absolute;left:520px;top:21px;width:56px;height:22px;background:var(--button-blue);color:var(--white);font-size:8.5px;font-weight:700;text-align:center;line-height:22px}
.section-title{font-family:'Montserrat',sans-serif;font-weight:700;font-size:12px;letter-spacing:3px}
.offers{top:400px;height:213px}
.offer{position:absolute;top:38px;width:179px}
.offer .photo{height:90px}
.offer h4{margin-top:10px;font-size:12px;font-weight:400;white-space:nowrap}
.offer h4 b{font-weight:700}
.offer p{margin-top:4px;font-size:7.6px;line-height:1.35;color:var(--text-light)}
.contact{top:617px;height:213px}
.contact address{position:absolute;left:18px;top:40px;font-style:normal;font-size:7.8px;line-height:1.5;white-space:nowrap}
.map{position:absolute;left:184px;top:39px;width:422px;height:152px;background:linear-gradient(135deg,#ece6d6,#e3dcc6 60%,#cfe0c0)}
.reviews{top:833px;height:174px}
.review-widget{position:absolute;left:17px;top:18px;width:282px;height:140px;background:var(--white);border:2px solid #c7dbb8;color:var(--ink);padding:5px 9px}
.review-widget .site{font-size:12px;font-weight:600;color:#222;line-height:1.2}
.review-widget .count{font-size:7px;font-style:italic;color:var(--muted);margin-top:3px;padding-bottom:5px;border-bottom:1px solid #ddd;white-space:nowrap}
.review-widget .count u{color:var(--link-blue)}
.review-widget h5{font-size:9px;font-weight:700;margin-top:7px}
.review-widget .rating-label{font-size:7px;font-weight:700;margin-top:5px}
.review-widget svg{display:block;margin-top:2px}
.review-widget .small{font-size:6.5px;color:var(--muted);margin-top:2px}
.review-widget .links{font-size:6.5px;color:var(--link-blue);text-decoration:underline;margin-top:6px}
.review-widget .copy{margin-top:7px}
.hotel-front{position:absolute;left:315px;top:18px;width:291px;height:140px;background:linear-gradient(180deg,#efe9dc,#d8d2c4 60%,#2a2a2a)}
.footer-bar{top:1010px;height:52px}
.footer-nav{position:absolute;left:17px;top:22px;display:flex;gap:13px}
.social{position:absolute;right:18px;top:19px;display:flex;gap:12px;font-size:9px;font-weight:700;white-space:nowrap}
</style>
</head>
<body>
<div class="backdrop" role="img" aria-label="Aerial photograph of central London rooftops and parks"></div>

<div class="brand-mark abs" style="left:392px;top:10px"><span class="name">Restwell<br>Inn</span></div>
<div class="place-title abs" style="left:497px;top:49px;color:#222">LONDON - VICTORIA</div>

<nav class="section main-nav">
  <a>HOME</a><a>OUR ROOMS</a><a>ATTRACTIONS</a><a>LONDON EVENTS</a><a>SPECIAL OFFERS</a><a>PHOTOS</a><a>DIRECTIONS</a><a>CONTACT</a>
</nav>

<section class="section hero" role="img" aria-label="Hotel room with sofa, colourful cushions and a yellow chair">
  <div class="caption">
    <h2>LOREM IPSUM DOLOR SIT AMET</h2>
    <p>Lorem ipsum dolor sit amet, consectetuer adipiscing elit,<br>sed diam nonummy nibh euismod tincidunt</p>
  </div>
</section>
<svg class="slide-arrow" style="left:129px" viewBox="0 0 22 22"><circle cx="11" cy="11" r="11" fill="#6b6b6b" opacity=".8"/><path d="M13 6l-5 5 5 5" stroke="#fff" stroke-width="1.5" fill="none"/></svg>
<svg class="slide-arrow" style="left:708px" viewBox="0 0 22 22"><circle cx="11" cy="11" r="11" fill="#fff"/><path d="M9 6l5 5-5 5" stroke="#e8a21c" stroke-width="1.5" fill="none"/></svg>

<section class="section booking-band">
  <div class="booking">
    <h3>BOOK A ROOM</h3>
    <div class="intro">Lorem ipsum solor sid ahmed loresin vane.</div>
    <span class="field-label" style="left:142px">Type of room:</span>
    <div class="field" style="left:142px;width:105px">Select a type of room ▾</div>
    <span class="field-label" style="left:254px">Check-in date:</span>
    <div class="field" style="left:254px;width:87px">DD/MM/YYYY</div>
    <span class="field-label" style="left:348px">Check-out date:</span>
    <div class="field" style="left:348px;width:86px">DD/MM/YYYY</div>
    <span class="field-label" style="left:442px">Adults:</span>
    <div class="field" style="left:442px;width:32px">1 ▾</div>
    <span class="field-label" style="left:481px">Children:</span>
    <div class="field" style="left:481px;width:31px">0 ▾</div>
    <div class="book-btn">Book now</div>
  </div>
</section>

<section class="section offers">
  <h2 class="section-title abs" style="left:17px;top:13px">SPECIAL OFFERS</h2>
  <article class="offer" style="left:17px">
    <div class="photo" role="img" aria-label="Hotel bedroom with red cushions" style="background:linear-gradient(160deg,#d9b34a,#e9dcb0 55%,#8a1f1f)"></div>
    <h4><b>25% off</b> on Spa Treatments</h4>
    <p>Lorem ipsum dolor sit amet, consectetuer adipiscing elit, sed diam nonummy nibh euismod tincidunt ut laoreet dolore magna aliquam erat volutpat.</p>
  </article>
  <article class="offer" style="left:224px">
    <div class="photo" role="img" aria-label="Guards band parade in red tunics" style="background:linear-gradient(160deg,#8a9a7e,#c23a2a 55%,#2a2a2a)"></div>
    <h4>Sunday <b>Special</b></h4>
    <p>Lorem ipsum dolor sit amet, consectetuer adipiscing elit, sed diam nonummy nibh euismod tincidunt ut laoreet dolore magna aliquam erat volutpat.</p>
  </article>
  <article class="offer" style="left:427px">
    <div class="photo" role="img" aria-label="Clock tower against blue sky" style="background:linear-gradient(160deg,#3a64b8,#7fa0d8 45%,#8a6a3a)"></div>
    <h4><b>Shopping</b> in London</h4>
    <p>Lorem ipsum dolor sit amet, consectetuer adipiscing elit, sed diam nonummy nibh euismod tincidunt ut laoreet dolore magna aliquam erat volutpat.</p>
  </article>
</section>

<section class="section contact">
  <h2 class="section-title abs" style="left:18px;top:13px">CONTACT</h2>
  <address>42-48 Harrowdene Road<br>Victoria - London<br>SW1X 4RB<br><br>Email: stay@restwellmarlow.co.uk<br>Tel.&nbsp;&nbsp;&nbsp;+44 (0) 20 7946 0123<br>Fax:&nbsp;&nbsp;+44 (0) 20 7946 0456</address>
  <div class="map" role="img" aria-label="Street map showing the hotel location near Victoria station"></div>
</section>

<section class="section reviews">
  <div class="review-widget">
    <div class="site">Journeyscope</div>
    <div class="count">378 reviews of <u>Restwell Inn London - Victoria</u> in London</div>
    <h5>Restwell Inn London - Victoria</h5>
    <div class="rating-label">Journeyscope Traveller Rating:</div>
    <svg width="60" height="11" viewBox="0 0 60 11">
      <g stroke="var(--review-green)" stroke-width="1.2"><circle cx="5.5" cy="5.5" r="4.5" fill="var(--review-green)"/><circle cx="17" cy="5.5" r="4.5" fill="var(--review-green)"/><circle cx="28.5" cy="5.5" r="4.5" fill="var(--review-green)"/><circle cx="40" cy="5.5" r="4.5" fill="var(--review-green)"/><circle cx="51.5" cy="5.5" r="4.5" fill="none"/></g>
    </svg>
    <div class="small">Based on 378 traveller reviews</div>
    <div class="links">Read reviews &nbsp;|&nbsp; Write a review</div>
    <div class="small copy">© 2013 Journeyscope Ltd</div>
  </div>
  <div class="hotel-front" role="img" aria-label="Hotel entrance with white facade, railings and flower boxes"></div>
</section>

<footer class="section footer-bar">
  <nav class="footer-nav"><a>HOME</a><a>CONTACT</a></nav>
  <div class="social"><span>Journeyscope</span><span>Plusring</span><span>Chirpr</span><span>Facefolio</span><span>Pinwall</span></div>
</footer>

<div class="brand-mark abs" style="left:385px;top:1073px"><span class="name">Restwell<br>Inn</span></div>
<div class="place-title abs" style="left:489px;top:1111px;color:var(--white)">LONDON - VICTORIA</div>
</body>
</html>
```